Home page design for Drone video business (the Business focusses on home videos for realtors)

Dear reader,

*I NEED DESIGNS OF ALL THE PAGES*
We need a first design of a homepage and of 4 other pages of the website of a business that sells drone video services. All the pages will need to be in the similar design style.
The video's are targeted at consumers that want to sell there home and would like to have a cool drone video of photos of their home.

How does the website look:
- has a navbar on top
- A cool looking banner of an areal drone.
- A Big header: with company name: SkyNestReels
- A smaller subheader: We film your home to increase your chances of sale
- Then a section with a Big header: How does it work
- In this section a place for a vimeo explainitory video
- Then a similar navbar styled bar with a phone number and a email address
- Then a section where the videos porfolio is displayed in a cool way
- Inside this sectiona header: Our work

- A section with header: Why us?
- 4 symbols here with a subheader and some lorum ipsum text underneath (see wireframe images)

- Under that a: Contact us
- where you can put in name, email, phone, message box and a send button

- At the bottom a footer with phone number and a fake address for now.

Be creative. Use creative but serious color.
Use a serious font. Make it a sharp design. Sharp lines. Not to dark design and not to light design.

The wireframes are the same kind of images.
PLEASE PUT IN DESIGNS OF ALL THE PAGES

Good luck

Target Market(s)

People that want to sell home and want to make a cool drone video or photos of their home.

Industry/Entity Type

Business

Contact Information for Business Card

Milo Brenning
milo@skynestreels.example
+31647283915

Logo Text

SkyNestReels

Number of Pages Required

1 page

Font styles to use
Sans Serif

Requirements
Must have
• All the sections as explained in the instructions.
• The nav bar should have an about us, services, portfolio and a contact us buttons.
• See instruction for details.
• Must include designs of the front page, contact us, our services, portfolio and contact us.
• If you do add some designs for the "about us", "services", "prices", "portfolio" and "contact us" pages, you make a way better chance of winning the competition.
Nice to have
• designs for the other pages as described at the Must haves. You make a better chance of winning if you include them. Look at the wireframes to see the mockups for those pages. think creative about what kind of sections and design should be included in those pages.
Should not have
• bad designs.

```html
<!DOCTYPE html>
<html lang="en">
<head>
<meta charset="utf-8">
<title>SkyNestReels – Home</title>
<link rel="stylesheet" href="https://fonts.googleapis.com/css2?family=Open+Sans:wght@400;600;700;800&display=swap">
<style>
:root{
  --accent:#fbb400;
  --ink:#444444;
  --dark:#1f1f1f;
  --darker:#111111;
  --band:#efefef;
  --white:#ffffff;
  --muted:#666666;
  --field-line:#6b6b6b;
}
*{box-sizing:border-box;margin:0;padding:0}
html,body{width:1200px;height:2568px;overflow:hidden}
body{position:relative;font-family:"Open Sans",Arial,sans-serif;background:var(--white);color:var(--ink)}
.abs{position:absolute}

/* hero */
.hero{left:0;top:0;width:1200px;height:657px;background:linear-gradient(180deg,#7d7468 0%,#8a7a66 35%,#6f6457 70%,#5a524a 100%)}
.hero-shade{left:0;top:0;width:1200px;height:657px;background:rgba(0,0,0,.18)}
.nav{left:0;top:0;width:1200px;height:74px;background:rgba(60,60,60,.55);border-bottom:1px solid rgba(255,255,255,.25)}
.brand{left:60px;top:0;width:258px;height:74px;border-right:1px solid rgba(255,255,255,.25);display:flex;align-items:center;gap:10px;padding-left:40px}
.brand-dot{width:14px;height:14px;border-radius:50%;background:var(--accent)}
.brand-name{font-weight:700;font-size:22px;color:var(--white)}
.nav-link{top:28px;font-size:12px;font-weight:700;color:var(--white);text-transform:uppercase}
.nav-link.active{color:var(--accent)}
.hero-title{left:0;width:1200px;top:264px;text-align:center;font-size:62px;font-weight:700;color:var(--white);letter-spacing:1px}
.hero-sub{left:0;width:1200px;top:345px;text-align:center;font-size:30px;font-weight:700;color:var(--white);line-height:38px}
.hero-arrow{top:300px}

/* sections */
.section-title{left:0;width:1200px;text-align:center;font-size:36px;font-weight:800;color:var(--ink);letter-spacing:1px}
.video-frame{left:226px;top:774px;width:748px;height:358px;background:linear-gradient(180deg,#8fa3b8 0%,#7b8fa3 60%,#4e5f52 100%)}
.play{position:absolute;width:77px;height:55px;border-radius:10px;background:var(--white);display:flex;align-items:center;justify-content:center}
.play.small{width:40px;height:28px;border-radius:6px}

/* contact strip */
.strip-dark{left:0;top:1166px;width:600px;height:56px;background:var(--dark)}
.strip-accent{left:600px;top:1166px;width:600px;height:56px;background:var(--accent)}
.strip-badge{left:580px;top:1174px;width:40px;height:40px;border-radius:50%;background:var(--white)}
.strip-text{top:1166px;height:56px;font-weight:700;color:var(--white);display:flex;align-items:center;gap:16px;white-space:nowrap}
.strip-text.phone{left:243px;font-size:27px}
.strip-text.mail{left:649px;font-size:21px;gap:14px}

/* work */
.thumb{top:1346px;width:242px;height:186px}
.work-arrow{top:1424px}

/* why */
.why{left:0;top:1604px;width:1200px;height:461px;background:var(--band)}
.feature-icon{width:90px;height:90px;border-radius:50%;background:var(--accent);display:flex;align-items:center;justify-content:center}
.feature-title{font-size:17px;font-weight:700;color:var(--accent);text-transform:uppercase}
.feature-text{width:395px;font-size:15px;line-height:23px;color:var(--muted)}

/* contact */
.contact{left:0;top:2065px;width:1200px;height:435px;background:linear-gradient(180deg,#1c1f22 0%,#141618 100%)}
.contact-title{left:0;width:1200px;top:2118px;text-align:center;font-size:34px;font-weight:700;color:var(--white)}
.field{left:253px;width:332px;height:42px;border:1px solid var(--field-line);border-radius:21px;padding:0 26px;font-size:13px;color:#dddddd;display:flex;align-items:center}
.field.message{left:613px;top:2205px;width:423px;height:94px;border-radius:22px;align-items:flex-start;padding-top:14px}
.send{left:613px;top:2311px;width:423px;height:42px;border-radius:21px;background:var(--accent);color:var(--white);font-size:15px;font-weight:700;display:flex;align-items:center;justify-content:center;letter-spacing:1px}
.rule{left:75px;top:2388px;width:1050px;height:1px;background:#3a3a3a}
.info-label{top:2413px;font-size:15px;font-weight:700;color:var(--accent)}
.info-value{top:2438px;height:34px;font-weight:700;color:var(--white);display:flex;align-items:center;gap:12px;white-space:nowrap}

/* bottom */
.bottom{left:0;top:2500px;width:1200px;height:68px;background:var(--darker)}
.copyright{left:75px;top:2526px;font-size:11px;color:#9a9a9a}
.social{top:2527px;width:14px;height:14px;border-radius:50%;background:#8a8a8a}
</style>
</head>
<body>

<!-- hero -->
<div class="abs hero" role="img" aria-label="Aerial photo of a town taken from a white drone, its rotor arms framing the view"></div>
<div class="abs hero-shade"></div>

<header class="abs nav">
  <div class="abs brand"><span class="brand-dot"></span><span class="brand-name">SkyNestReels</span></div>
  <span class="abs nav-link active" style="left:628px">Home</span>
  <span class="abs nav-link" style="left:714px">Services</span>
  <span class="abs nav-link" style="left:818px">About us</span>
  <span class="abs nav-link" style="left:929px">Portfolio</span>
  <span class="abs nav-link" style="left:1048px">Contact us</span>
</header>

<h1 class="abs hero-title">SKYNESTREELS</h1>
<p class="abs hero-sub">We film your home to increase your<br>chances of sale</p>
<svg class="abs hero-arrow" style="left:76px" width="28" height="56" viewBox="0 0 28 56"><polyline points="26,2 2,28 26,54" fill="none" stroke="#fff" stroke-width="3"/></svg>
<svg class="abs hero-arrow" style="left:1096px" width="28" height="56" viewBox="0 0 28 56"><polyline points="2,2 26,28 2,54" fill="none" stroke="#fff" stroke-width="3"/></svg>

<!-- how it works -->
<h2 class="abs section-title" style="top:697px">HOW DOES IT WORK</h2>
<div class="abs video-frame" role="img" aria-label="Explainer video still: a large camera drone hovering above its pilot against the sky">
  <div class="play" style="left:336px;top:152px">
    <svg width="22" height="24" viewBox="0 0 22 24"><polygon points="2,1 21,12 2,23" fill="#222"/></svg>
  </div>
</div>

<!-- contact strip -->
<div class="abs strip-dark"></div>
<div class="abs strip-accent"></div>
<div class="abs strip-badge"></div>
<div class="abs strip-text phone">
  <svg width="24" height="24" viewBox="0 0 24 24"><path d="M6.6 10.8c1.4 2.8 3.8 5.1 6.6 6.6l2.2-2.2c.3-.3.7-.4 1-.2 1.1.4 2.3.6 3.6.6.6 0 1 .4 1 1V20c0 .6-.4 1-1 1C10.6 21 3 13.4 3 4c0-.6.4-1 1-1h3.5c.6 0 1 .4 1 1 0 1.3.2 2.5.6 3.6.1.3 0 .7-.2 1z" fill="#fff"/></svg>
  +31 64 72 83 915
</div>
<div class="abs strip-text mail">
  <svg width="26" height="20" viewBox="0 0 28 22"><rect x="1" y="1" width="26" height="20" rx="2" fill="#fff"/><polyline points="2,3 14,12 26,3" fill="none" stroke="#fbb400" stroke-width="2.5"/></svg>
  CONTACT@SKYNESTREELS.EXAMPLE
</div>

<!-- our work -->
<h2 class="abs section-title" style="top:1262px">OUR WORK</h2>
<svg class="abs work-arrow" style="left:44px" width="16" height="30" viewBox="0 0 16 30"><polyline points="14,2 2,15 14,28" fill="none" stroke="#555" stroke-width="3"/></svg>
<svg class="abs work-arrow" style="left:1140px" width="16" height="30" viewBox="0 0 16 30"><polyline points="2,2 14,15 2,28" fill="none" stroke="#555" stroke-width="3"/></svg>

<div class="abs thumb" style="left:75px;background:linear-gradient(135deg,#4a3a30,#9a8e80 60%,#5a4a3e)" role="img" aria-label="Portfolio video: interior of a living room with bay windows">
  <div class="play small" style="left:101px;top:79px"><svg width="12" height="14" viewBox="0 0 12 14"><polygon points="1,1 11,7 1,13" fill="#222"/></svg></div>
</div>
<div class="abs thumb" style="left:344px;background:linear-gradient(180deg,#5d8fc8 0%,#7ea55a 40%,#5f8a3a 100%)" role="img" aria-label="Portfolio video: aerial view of a white farmhouse in green fields">
  <div class="play small" style="left:101px;top:79px"><svg width="12" height="14" viewBox="0 0 12 14"><polygon points="1,1 11,7 1,13" fill="#222"/></svg></div>
</div>
<div class="abs thumb" style="left:615px;background:linear-gradient(180deg,#b8c4d0 0%,#b07a6a 40%,#5a8a3e 100%)" role="img" aria-label="Portfolio video: aerial view of a residential neighbourhood with red roofs">
  <div class="play small" style="left:101px;top:79px"><svg width="12" height="14" viewBox="0 0 12 14"><polygon points="1,1 11,7 1,13" fill="#222"/></svg></div>
</div>
<div class="abs thumb" style="left:883px;background:linear-gradient(180deg,#7fb2e0 0%,#8a7a6c 35%,#d8d0bc 70%,#c8c0aa 100%)" role="img" aria-label="Portfolio video: drone filming the siding and windows of a house">
  <div class="play small" style="left:101px;top:79px"><svg width="12" height="14" viewBox="0 0 12 14"><polygon points="1,1 11,7 1,13" fill="#222"/></svg></div>
</div>

<!-- why us -->
<section class="abs why"></section>
<h2 class="abs section-title" style="top:1657px">WHY US?</h2>

<div class="abs feature-icon" style="left:75px;top:1746px">
  <span style="color:#fff;font-size:40px;font-weight:700">$</span>
</div>
<h3 class="abs feature-title" style="left:190px;top:1742px">Cheap</h3>
<p class="abs feature-text" style="left:190px;top:1771px">Lorem ipsum dolor sit amet, consect etuer adipiscing elit, sed diam nonummy liquam nibh a dui iaculis viverra id a velit...</p>

<div class="abs feature-icon" style="left:614px;top:1746px">
  <svg width="40" height="36" viewBox="0 0 40 36" fill="none" stroke="#fff" stroke-width="3"><line x1="4" y1="8" x2="36" y2="8"/><line x1="4" y1="18" x2="36" y2="18"/><line x1="4" y1="28" x2="36" y2="28"/><rect x="10" y="4" width="6" height="8" fill="#fbb400"/><rect x="24" y="14" width="6" height="8" fill="#fbb400"/><rect x="14" y="24" width="6" height="8" fill="#fbb400"/></svg>
</div>
<h3 class="abs feature-title" style="left:729px;top:1742px">Flexible</h3>
<p class="abs feature-text" style="left:729px;top:1771px">Lorem ipsum dolor sit amet, consect etuer adipiscing elit, sed diam nonummy liquam nibh a dui iaculis viverra id a velit...</p>

<div class="abs feature-icon" style="left:75px;top:1898px">
  <svg width="36" height="36" viewBox="0 0 36 36" fill="#fff"><rect x="3" y="15" width="7" height="17" rx="1"/><path d="M13 16 L20 4 c2 -1 4 0 4 2 L22 13 H31 c2 0 3 2 2.6 3.5 L30 30 c-.4 1.3-1.5 2-2.8 2 H13z"/></svg>
</div>
<h3 class="abs feature-title" style="left:190px;top:1894px">Quality</h3>
<p class="abs feature-text" style="left:190px;top:1923px">Lorem ipsum dolor sit amet, consect etuer adipiscing elit, sed diam nonummy liquam nibh a dui iaculis viverra id a velit...</p>

<div class="abs feature-icon" style="left:614px;top:1898px">
  <svg width="40" height="36" viewBox="0 0 40 36" fill="none" stroke="#fff" stroke-width="3"><polyline points="3,3 3,33 37,33"/><polyline points="8,27 16,17 22,22 33,9"/><polyline points="26,9 33,9 33,16"/></svg>
</div>
<h3 class="abs feature-title" style="left:729px;top:1894px">Increase sale chance</h3>
<p class="abs feature-text" style="left:729px;top:1923px">Lorem ipsum dolor sit amet, consect etuer adipiscing elit, sed diam nonummy liquam nibh a dui iaculis viverra id a velit...</p>

<!-- contact -->
<section class="abs contact" role="img" aria-label="Dark background photo of a white quadcopter drone in flight"></section>
<h2 class="abs contact-title">CONTACT US</h2>
<div class="abs field" style="top:2205px">Name</div>
<div class="abs field" style="top:2258px">Phone No</div>
<div class="abs field" style="top:2311px">Email Address</div>
<div class="abs field message">Message</div>
<div class="abs send">SEND</div>
<div class="abs rule"></div>

<span class="abs info-label" style="left:98px">CALL US</span>
<div class="abs info-value" style="left:98px;font-size:26px">
  <svg width="22" height="22" viewBox="0 0 24 24"><path d="M6.6 10.8c1.4 2.8 3.8 5.1 6.6 6.6l2.2-2.2c.3-.3.7-.4 1-.2 1.1.4 2.3.6 3.6.6.6 0 1 .4 1 1V20c0 .6-.4 1-1 1C10.6 21 3 13.4 3 4c0-.6.4-1 1-1h3.5c.6 0 1 .4 1 1 0 1.3.2 2.5.6 3.6.1.3 0 .7-.2 1z" fill="#fff"/></svg>
  +31 64 72 83 915
</div>
<span class="abs info-label" style="left:462px">EMAIL US</span>
<div class="abs info-value" style="left:462px;font-size:17px">
  <svg width="24" height="18" viewBox="0 0 28 22"><rect x="1" y="1" width="26" height="20" rx="2" fill="#fff"/><polyline points="2,3 14,12 26,3" fill="none" stroke="#141618" stroke-width="2.5"/></svg>
  contact@skynestreels.example
</div>
<span class="abs info-label" style="left:813px">CONTACT INFO</span>
<div class="abs info-value" style="left:813px;font-size:16px">
  <svg width="24" height="18" viewBox="0 0 28 22"><rect x="1" y="1" width="26" height="20" rx="2" fill="#fff"/><polyline points="2,3 14,12 26,3" fill="none" stroke="#141618" stroke-width="2.5"/></svg>
  27 Larkfield Road, Glasgow
</div>

<!-- bottom bar -->
<footer class="abs bottom"></footer>
<span class="abs copyright">Copyright © 2016. Company Name. All Right Reserved</span>
<span class="abs social" style="left:987px"></span>
<span class="abs social" style="left:1018px"></span>
<span class="abs social" style="left:1049px"></span>
<span class="abs social" style="left:1080px"></span>
<span class="abs social" style="left:1111px"></span>

</body>
</html>
```